" Clínica médica que atua nas diversas especialidades e realiza atendimentos particulares a preços acessíveis, podendo futuramente atender planos de saúde. "

```html
<!DOCTYPE html>
<html lang="pt-BR">
<head>
<meta charset="utf-8">
<title>VivaMed — Clínica Médica</title>
<link href="https://fonts.googleapis.com/css2?family=Raleway:wght@400;500;600;700&family=Roboto+Condensed:wght@700&display=swap" rel="stylesheet">
<style>
  :root {
    --page-bg: #eeeeee;
    --green-deep: #0b4a33;
    --green-dark: #11603f;
    --green-mid: #2f8a4f;
    --green-hero: #5fb35a;
    --green-soft: #9fd08f;
    --teal: #1f8fa0;
    --white: #ffffff;
    --ink: #1f3b2e;
    --ink-soft: #6d7b73;
  }
  * { box-sizing: border-box; margin: 0; padding: 0; }
  html, body { width: 1200px; height: 1200px; overflow: hidden; }
  body {
    background: var(--page-bg);
    font-family: "Raleway", sans-serif;
    position: relative;
  }
  .site {
    position: absolute;
    left: 0; top: 280px;
    width: 1200px; height: 640px;
    background: var(--white);
    overflow: hidden;
  }
  /* Header */
  .site-header {
    position: absolute; left: 0; top: 0;
    width: 1200px; height: 100px;
    display: flex;
  }
  .brand {
    width: 224px; height: 100px;
    background: linear-gradient(135deg, var(--green-deep), var(--green-dark));
    display: flex; flex-direction: column; align-items: center; justify-content: center;
    color: var(--white);
  }
  .brand-row { display: flex; align-items: center; gap: 8px; }
  .brand-dot { width: 12px; height: 12px; border-radius: 50%; background: var(--green-soft); }
  .brand-name { font-size: 28px; font-weight: 600; letter-spacing: 0.2px; }
  .brand-tag { font-size: 10px; font-weight: 500; color: var(--green-soft); margin-top: 2px; letter-spacing: 1px; text-transform: uppercase; }

  .header-main { flex: 1; display: flex; flex-direction: column; }
  .info-bar {
    height: 24px;
    display: flex; align-items: center; justify-content: space-between;
    padding: 0 18px;
    font-size: 9.5px; color: var(--ink-soft);
    border-bottom: 1px solid #e3e8e5;
  }
  .info-bar span + span { border-left: 1px solid #d4dbd7; padding-left: 14px; }
  .main-nav {
    flex: 1;
    display: flex; align-items: center; justify-content: space-around;
    padding: 0 20px;
  }
  .main-nav a {
    text-decoration: none; color: var(--ink);
    font-size: 20px; font-weight: 500; text-align: center; line-height: 1.05;
  }
  .results-button {
    width: 214px; height: 100px;
    background: linear-gradient(135deg, var(--green-dark), var(--green-deep));
    color: var(--white);
    display: flex; align-items: center; justify-content: center; text-align: center;
    font-size: 19px; font-weight: 700; line-height: 1.15; text-transform: uppercase;
  }

  /* Hero */
  .hero {
    position: absolute; left: 0; top: 100px;
    width: 1200px; height: 526px;
    background: linear-gradient(90deg, var(--green-mid) 0%, var(--green-hero) 22%, #b6dca8 45%, #f3f6f2 70%, #ffffff 100%);
  }
  .hero-photo {
    position: absolute; left: 140px; top: 0;
    width: 1060px; height: 526px;
    background:
      radial-gradient(ellipse 200px 300px at 680px 330px, rgba(240,226,205,0.85), rgba(255,255,255,0) 70%),
      radial-gradient(ellipse 170px 280px at 970px 340px, rgba(232,236,238,0.9), rgba(255,255,255,0) 70%),
      radial-gradient(ellipse 150px 260px at 340px 360px, rgba(220,238,214,0.55), rgba(255,255,255,0) 70%);
  }
  .hero-title {
    position: absolute; left: 140px; top: 205px;
    font-family: "Roboto Condensed", sans-serif;
    font-weight: 700; font-size: 48px; line-height: 1.08;
    color: var(--white); text-transform: uppercase;
  }
  .slider-arrow {
    position: absolute; top: 250px;
    width: 34px; height: 34px;
    background: var(--green-deep);
    display: flex; align-items: center; justify-content: center;
  }
  .slider-arrow.prev { left: 16px; }
  .slider-arrow.next { right: 16px; }
  .accent-strip {
    position: absolute; left: 0; bottom: 0;
    width: 1200px; height: 14px;
    background: linear-gradient(90deg, var(--green-dark), var(--green-hero) 45%, var(--teal));
  }
</style>
</head>
<body>
  <div class="site">
    <header class="site-header">
      <div class="brand">
        <div class="brand-row">
          <span class="brand-dot"></span>
          <span class="brand-name">VivaMed</span>
        </div>
        <span class="brand-tag">Clínica Médica</span>
      </div>
      <div class="header-main">
        <div class="info-bar">
          <span>Agende sua consulta</span>
          <span>Atendimento: Seg a Sex, 7h às 19h</span>
          <span>contato@vivamed.com.br</span>
          <span>(00) 0000-0000</span>
        </div>
        <nav class="main-nav">
          <a href="#">Quem Somos</a>
          <a href="#">Consultas<br>e Tratamentos</a>
          <a href="#">Exames</a>
          <a href="#">Fale Conosco</a>
        </nav>
      </div>
      <div class="results-button">Resultados<br>de Exames</div>
    </header>

    <section class="hero">
      <div class="hero-photo" role="img" aria-label="Equipe de médicos sorridentes de jaleco branco, de braços cruzados"></div>
      <h1 class="hero-title">Viver bem é<br>estar bem</h1>
      <div class="slider-arrow prev">
        <svg width="14" height="14" viewBox="0 0 14 14"><path d="M9 2 L4 7 L9 12" fill="none" stroke="#ffffff" stroke-width="2"/></svg>
      </div>
      <div class="slider-arrow next">
        <svg width="14" height="14" viewBox="0 0 14 14"><path d="M5 2 L10 7 L5 12" fill="none" stroke="#ffffff" stroke-width="2"/></svg>
      </div>
    </section>
    <div class="accent-strip"></div>
  </div>
</body>
</html>
```